Brindle's Botanic's. I make and sell organic bath & body products. Nourishing bath & body products. Products are soaps, scrubs, lip balms, bath salts, baby & mother products (belly balm, nipple balm, diaper balm, baby bath soak, chest rub,) . I use botanical and or herbs in all my recipes. I create my own recipes. I like muted colors...but I would like something that will get your attention. I like the colors green and brown, but open to any other colors. I would also like to get information about labels (different sizes for my products) I do like the pasley print and maybe even a cute owl.

Target Market(s)

women, pregnant and nursing women, women with children and men

Industry/Entity Type

Baby

Contact Information for Business Card

Mona Greeley
517-384-2706,mgreeley@tallowmail.example
mgreeley@tallowmail.example

Font styles to use
Other font styles liked:
• bree

Requirements
Must have
• Brindle's Botanic's, nourishing bath & body products. It needs to get a person attention. I would like to see cards that are hip and fun. I would also like to view cards that are classy. I do like muted colors but I do have an open mind (use any color you think would be right) So far a lot of the cards have had leaves....I really do not like that design.
Nice to have
• ???pasley in the background ?cute owl
Should not have
• leaves

```html
<!DOCTYPE html>
<html lang="en">
<head>
<meta charset="utf-8">
<title>Brindle's Botanic's – Business Card</title>
<link rel="stylesheet" href="https://fonts.googleapis.com/css2?family=Fira+Sans:wght@400;500&display=swap">
<style>
  :root {
    --paper: #f1eee2;
    --band-green: #84ae0c;
    --brand-green: #7aa712;
    --leaf-deep: #6a9f08;
    --leaf-light: #8cbb1c;
    --earth-brown: #5a3214;
    --white: #ffffff;
  }
  html, body {
    margin: 0;
    padding: 0;
    overflow: hidden;
    background: var(--paper);
  }
  .card {
    position: relative;
    width: 1200px;
    height: 704px;
    overflow: hidden;
    background: var(--paper);
    font-family: "Fira Sans", Arial, sans-serif;
  }
  .card p, .card h1 {
    margin: 0;
    line-height: 1;
    white-space: nowrap;
  }
  .brand {
    position: absolute;
    left: 66px;
    top: 70px;
    display: flex;
    align-items: center;
    gap: 20px;
  }
  .brand-dot {
    width: 60px;
    height: 60px;
    border-radius: 50%;
    background: var(--brand-green);
  }
  .brand-name {
    font-size: 68px;
    font-weight: 500;
    color: var(--brand-green);
    line-height: 1;
  }
  .tagline {
    position: absolute;
    left: 90px;
    top: 187px;
    font-size: 42px;
    font-weight: 400;
    color: var(--earth-brown);
  }
  .contact-band {
    position: absolute;
    left: 0;
    top: 306px;
    width: 1200px;
    height: 239px;
    background: var(--band-green);
  }
  .person-name {
    position: absolute;
    left: 90px;
    top: 347px;
    font-size: 55px;
    font-weight: 500;
    color: var(--white);
  }
  .contact-line {
    position: absolute;
    left: 90px;
    font-size: 31px;
    font-weight: 400;
    color: var(--white);
  }
  .contact-phone { top: 425px; }
  .contact-email { top: 473px; }
  .website {
    position: absolute;
    left: 64px;
    top: 618px;
    font-size: 38px;
    font-weight: 400;
    letter-spacing: 2.5px;
    color: var(--brand-green);
  }
  .sprig-art {
    position: absolute;
    left: 700px;
    top: 236px;
    width: 484px;
    height: 454px;
  }
</style>
</head>
<body>
  <main class="card">
    <div class="brand">
      <span class="brand-dot"></span>
      <span class="brand-name">Brindle's Botanic's</span>
    </div>
    <p class="tagline">Nourishing bath &amp; body products</p>

    <div class="contact-band"></div>

    <svg class="sprig-art" viewBox="0 0 484 454" role="img" aria-label="Illustration of a green sprig with three large leaves">
      <defs>
        <radialGradient id="sprigTone" cx="0.5" cy="0.5" r="0.5">
          <stop offset="0" stop-color="var(--leaf-deep)" stop-opacity="0.85"/>
          <stop offset="0.7" stop-color="var(--leaf-light)" stop-opacity="0.55"/>
          <stop offset="1" stop-color="var(--leaf-light)" stop-opacity="0"/>
        </radialGradient>
      </defs>
      <ellipse cx="242" cy="227" rx="242" ry="227" fill="url(#sprigTone)"/>
    </svg>

    <h1 class="person-name">Mona Greeley</h1>
    <p class="contact-line contact-phone">Ph.: 517-384-2706</p>
    <p class="contact-line contact-email">E-mail: mgreeley@tallowmail.example</p>

    <p class="website">www.brindle'sbotanic's.com</p>
  </main>
</body>
</html>
```